Hair salon Business Card

Beauty Salon
I would like to see designs using sky blue and a soft orange. Mainly I would like my name ( Glow N' Wave Salon ) used as the design

Industry/Entity Type

Business

Contact Information for Business Card

Glow N'Wave Salon
418 E Birchfield Hyw #14
San Dimas, Ca 91748
909 527-6184

```html
<!DOCTYPE html>
<html lang="en">
<head>
<meta charset="utf-8">
<title>Glow N' Wave Salon – Business Card</title>
<link href="https://fonts.googleapis.com/css2?family=Arimo:wght@400;700&display=swap" rel="stylesheet">
<style>
  :root {
    --page-bg: #ffffff;
    --sky: #9fd6ef;
    --mist: #c4c4a8;
    --soft-orange: #f3a95c;
    --ink: #111111;
  }
  html, body {
    margin: 0;
    padding: 0;
    width: 1200px;
    height: 1200px;
    overflow: hidden;
    background: var(--page-bg);
    font-family: "Arimo", Arial, sans-serif;
    color: var(--ink);
  }
  .business-card {
    position: absolute;
    left: 330px;
    top: 442px;
    width: 540px;
    height: 315px;
    overflow: hidden;
  }
  .card-background {
    position: absolute;
    inset: 0;
    background: linear-gradient(125deg, var(--sky) 0%, var(--mist) 48%, var(--soft-orange) 100%);
  }
  .brand-name {
    position: absolute;
    left: 0;
    right: 0;
    top: 118px;
    text-align: center;
    font-size: 44px;
    font-weight: 400;
    letter-spacing: 1px;
    line-height: 1;
  }
  .rule-label {
    position: absolute;
    left: 91px;
    width: 358px;
    display: flex;
    align-items: center;
    gap: 5px;
    font-weight: 700;
    font-size: 14px;
    letter-spacing: 0.3px;
  }
  .rule-label::before,
  .rule-label::after {
    content: "";
    flex: 1;
    height: 1px;
    background: var(--ink);
  }
  .salon-tag { top: 174px; }
  .owner-name { top: 258px; }
  .contact-line {
    position: absolute;
    left: 91px;
    width: 358px;
    top: 283px;
    display: flex;
    align-items: center;
    justify-content: center;
    gap: 3px;
    font-size: 11.5px;
    white-space: nowrap;
  }
  .contact-icon { width: 11px; height: 11px; flex: none; }
  .phone-icon { margin-left: 3px; }
</style>
</head>
<body>
  <div class="business-card">
    <div class="card-background" role="img" aria-label="Sky blue to soft orange gradient with a faint pattern of beauty and hair care items"></div>

    <div class="brand-name">Glow N' Wave</div>
    <div class="rule-label salon-tag">SALON</div>

    <div class="rule-label owner-name">CORINNE</div>
    <div class="contact-line">
      <svg class="contact-icon" viewBox="0 0 12 12" aria-hidden="true">
        <circle cx="6" cy="6" r="6" fill="#111"/>
        <path d="M6 2.2a2.4 2.4 0 0 0-2.4 2.4C3.6 6.4 6 9.6 6 9.6s2.4-3.2 2.4-5A2.4 2.4 0 0 0 6 2.2z" fill="#fff"/>
        <circle cx="6" cy="4.6" r="0.9" fill="#111"/>
      </svg>
      <span class="address">418 E Birchfield Hyw #14,San Dimas, Ca 91748</span>
      <svg class="contact-icon phone-icon" viewBox="0 0 12 12" aria-hidden="true">
        <circle cx="6" cy="6" r="6" fill="#111"/>
        <rect x="4" y="2.3" width="4" height="7.4" rx="0.8" fill="#fff"/>
        <rect x="4.7" y="3.2" width="2.6" height="4.8" fill="#111"/>
      </svg>
      <span class="phone">909 527-6184</span>
    </div>
  </div>
</body>
</html>
```